Exercise Physiologist needs a Brochure

I am Exercise Physiologist providing exercise therapy for a variety of conditions. I have a logo and recent business card design. I like the black background like the front of the business cards. I have attached the flyer information required. I have also attached a few photos however they do not have to be used, happy to have no photos at all.

Industry/Entity Type

Health And Wellness

Font styles to use
Sans Serif

Requirements
Must have
• Please also add instagram @morvalecare
Nice to have
• tri-fold brochure

```html
<!DOCTYPE html>
<html lang="en">
<head>
<meta charset="utf-8">
<title>Morvale Health – Tri-fold Brochure</title>
<link rel="stylesheet" href="https://fonts.googleapis.com/css2?family=Open+Sans:wght@400;600;700;800&display=swap">
<style>
:root{
  --bg:#262626;
  --navy:#0c3d70;
  --blue:#1768b8;
  --sky:#3a9ee0;
  --pale:#eef1f4;
  --paper:#ffffff;
  --ink:#222a33;
  --muted:#5d6670;
}
*{box-sizing:border-box;margin:0;padding:0}
html,body{width:800px;height:1200px;overflow:hidden;background:var(--bg);font-family:"Open Sans",sans-serif;color:var(--ink)}
.spread{position:absolute;left:30px;width:740px;height:540px;display:grid;grid-template-columns:repeat(3,1fr);box-shadow:0 10px 30px rgba(0,0,0,.5)}
.spread--outside{top:30px}
.spread--inside{top:630px}
.panel{position:relative;overflow:hidden;background:var(--paper)}
.panel + .panel{border-left:1px solid #d8dde2}
.panel--grey{background:linear-gradient(#f2f4f6,#e4e8ec)}
.deco{position:absolute;inset:0;width:100%;height:100%}
.layer{position:absolute;left:0;right:0}
.photo{position:absolute;border-radius:50%;border:6px solid var(--sky)}
.photo--gym{left:48px;top:285px;width:150px;height:150px;background:radial-gradient(circle at 40% 40%,#9fb3c4,#3c5264 70%,#1e2f3d)}
.photo--legs{left:80px;top:14px;width:120px;height:120px;border-color:var(--navy);background:linear-gradient(160deg,#5a6d58,#7ea35c 60%,#4f6e3a)}
.photo--portrait{left:30px;top:372px;width:140px;height:140px;border-color:var(--blue);background:radial-gradient(circle,#5fb0ea,#2a7fcf);display:flex;align-items:center;justify-content:center;color:#fff;font-size:11px;font-weight:700;text-align:center}
.photo--silhouette{position:absolute;left:58px;top:24px;width:130px;height:110px;border-radius:50%;background:radial-gradient(circle,#d6dbe0,#eceff2 70%)}
.photo--knee{position:absolute;left:0;right:0;top:62px;height:270px;background:radial-gradient(circle at 55% 45%,#e88a8a 0,#b9a8a8 18%,#8d8d8d 45%,#5c5c5c 100%)}
.photo--runners{position:absolute;left:0;right:0;top:290px;height:250px;background:linear-gradient(#a9d3ec,#d8ebf5 45%,#7fb0cf 60%,#e8e2d6)}
.kicker{font-size:17px;font-weight:400;color:var(--ink);line-height:1.1}
.headline{font-weight:800;color:var(--blue);text-transform:uppercase;font-size:19px;line-height:1.1}
.body{font-size:9.5px;line-height:1.45;color:var(--ink)}
.phone-line{display:flex;align-items:center;gap:8px;color:#fff;font-weight:700}
.phone-line svg{flex:none}
.contact{position:absolute;left:18px;right:18px;top:160px;text-align:center}
.contact .cta{font-size:10.5px;font-weight:800;text-transform:uppercase;line-height:1.3}
.contact .cta strong{display:block;color:var(--blue);font-size:17px;font-style:italic}
.contact .row{display:flex;align-items:center;justify-content:center;gap:6px;font-size:9.5px;margin-top:8px}
.contact .addr{font-size:9px;margin-top:6px;line-height:1.35}
.dot{width:10px;height:10px;border-radius:50%;flex:none}
.dot--blue{background:var(--navy)}
.dot--pink{background:#c8326e}
.brand{position:absolute;left:26px;top:18px;display:flex;align-items:center;gap:8px}
.brand__ring{width:30px;height:30px;border-radius:50%;border:3px solid var(--blue)}
.brand__name{font-size:22px;font-weight:600;color:var(--blue)}
.brand__sub{position:absolute;left:64px;top:44px;font-size:6.5px;font-weight:600;color:var(--blue);letter-spacing:.5px;text-transform:uppercase}
.tagline{position:absolute;right:18px;top:388px;color:#fff;text-align:right;font-size:16px;line-height:1.1}
.tagline b{display:block;font-weight:800;text-transform:uppercase}
.name{font-size:21px;font-weight:700;color:var(--blue)}
.role{font-size:12px}
.creds{font-size:9px;line-height:1.4;margin-top:10px}
.heal{font-size:14px;margin-top:12px}
.heal b{color:var(--blue)}
.quote{position:relative;font-size:8.5px;line-height:1.4;margin-top:12px;padding:10px 18px 12px 20px;color:var(--muted)}
.quote::before,.quote::after{position:absolute;font-size:34px;font-weight:800;color:#9aa4ae;line-height:1}
.quote::before{content:"\201C";left:0;top:-4px}
.quote::after{content:"\201D";right:0;bottom:-18px}
.conditions{list-style:none;font-size:10px;font-weight:700;line-height:1.55;margin-top:10px}
.conditions li{display:flex;gap:6px}
.conditions li::before{content:"";width:7px;height:7px;margin-top:5px;border-radius:50%;background:var(--sky);flex:none}
</style>
</head>
<body>

<!-- OUTSIDE -->
<section class="spread spread--outside">

  <article class="panel panel--about">
    <svg class="deco" viewBox="0 0 247 540" preserveAspectRatio="none" aria-hidden="true">
      <path d="M0 405 Q120 370 247 392 L247 540 L0 540Z" fill="var(--sky)"/>
      <path d="M0 432 Q130 398 247 418 L247 540 L0 540Z" fill="var(--navy)"/>
    </svg>
    <div class="layer" style="top:28px;padding:0 20px">
      <p class="kicker">What is an</p>
      <h2 class="headline">Exercise<br>Physiologist?</h2>
      <p class="body" style="margin-top:14px">Exercise Physiologists are university educated health professionals trained to provide exercise therapy for pain and injury, pre and post surgery, mental health and chronic disease. They are registered providers with transport and workplace insurers, Publicare, the Veterans Support Office and many Private Health funds.</p>
    </div>
    <div class="photo photo--gym" role="img" aria-label="Photo of a rack of gym dumbbells"></div>
    <div class="layer phone-line" style="top:488px;padding-left:22px;font-size:22px">
      <svg width="18" height="18" viewBox="0 0 24 24"><circle cx="12" cy="12" r="11" fill="none" stroke="#fff" stroke-width="2"/><path d="M8 6c-1 1-1 3 1 6s4 5 6 5l1.5-1.5-2-2-1.5.8c-1-.6-2.2-1.8-2.8-2.8l.8-1.5-2-2z" fill="#fff"/></svg>
      0400 555 019
    </div>
  </article>

  <article class="panel panel--grey panel--contact">
    <svg class="deco" viewBox="0 0 247 540" preserveAspectRatio="none" aria-hidden="true">
      <path d="M0 440 Q130 405 247 425 L247 540 L0 540Z" fill="var(--sky)"/>
      <path d="M0 462 Q130 430 247 450 L247 540 L0 540Z" fill="var(--navy)"/>
    </svg>
    <div class="photo--silhouette" role="img" aria-label="Silhouette illustration of a person holding a side plank"></div>
    <div class="contact">
      <p class="cta">Call or email me today<br>to see how <strong>I can help you</strong></p>
      <div class="row"><svg width="14" height="14" viewBox="0 0 24 24"><circle cx="12" cy="12" r="11" fill="none" stroke="var(--blue)" stroke-width="1.5"/><path d="M12 5a4 4 0 0 0-4 4c0 3 4 8 4 8s4-5 4-8a4 4 0 0 0-4-4zm0 5.5a1.5 1.5 0 1 1 0-3 1.5 1.5 0 0 1 0 3z" fill="var(--blue)"/></svg></div>
      <p class="addr">Unit 4, 18 Harbour Lane WESTPORT<br>(Fenwick Fitness)</p>
      <div class="row" style="font-weight:700;font-size:11px">
        <svg width="12" height="12" viewBox="0 0 24 24"><circle cx="12" cy="12" r="11" fill="none" stroke="var(--ink)" stroke-width="2"/><path d="M8 6c-1 1-1 3 1 6s4 5 6 5l1.5-1.5-2-2-1.5.8c-1-.6-2.2-1.8-2.8-2.8l.8-1.5-2-2z" fill="var(--ink)"/></svg>
        0400 555 019
      </div>
      <div class="row"><svg width="13" height="10" viewBox="0 0 26 18"><rect x="1" y="1" width="24" height="16" fill="none" stroke="var(--ink)" stroke-width="1.6"/><path d="M1 1l12 9 12-9" fill="none" stroke="var(--ink)" stroke-width="1.6"/></svg>morvalecare@mailbox.com</div>
      <div class="row" style="font-size:8.5px"><span class="dot dot--blue"></span>morvalecare.net/social</div>
      <div class="row" style="font-size:8.5px"><span class="dot dot--pink"></span>@morvalecare</div>
    </div>
  </article>

  <article class="panel panel--cover">
    <svg class="deco" viewBox="0 0 247 540" preserveAspectRatio="none" aria-hidden="true">
      <path d="M0 70 Q120 40 247 58 L247 74 Q120 60 0 90Z" fill="var(--blue)"/>
      <path d="M0 395 Q120 350 247 330 L247 540 L0 540Z" fill="var(--sky)"/>
      <path d="M0 412 Q120 370 247 352 L247 540 L0 540Z" fill="var(--blue)"/>
      <path d="M0 455 Q130 430 247 440 L247 540 L0 540Z" fill="var(--navy)"/>
    </svg>
    <div class="photo--knee" role="img" aria-label="Black and white photo of hands holding a painful knee, highlighted red" style="clip-path:polygon(0 10%,100% 0,100% 100%,0 100%)"></div>
    <svg class="deco" viewBox="0 0 247 540" preserveAspectRatio="none" aria-hidden="true">
      <path d="M0 395 Q120 350 247 330 L247 540 L0 540Z" fill="var(--sky)"/>
      <path d="M0 412 Q120 370 247 352 L247 540 L0 540Z" fill="var(--blue)"/>
      <path d="M0 455 Q130 430 247 440 L247 540 L0 540Z" fill="var(--navy)"/>
    </svg>
    <div class="brand"><span class="brand__ring"></span><span class="brand__name">Morvale</span></div>
    <p class="brand__sub">Health &amp; Rehabilitation</p>
    <p class="tagline">Heal through <b>Movement</b></p>
    <div class="layer phone-line" style="top:486px;justify-content:center;font-size:19px">
      <svg width="16" height="16" viewBox="0 0 24 24"><circle cx="12" cy="12" r="11" fill="none" stroke="#fff" stroke-width="2"/><path d="M8 6c-1 1-1 3 1 6s4 5 6 5l1.5-1.5-2-2-1.5.8c-1-.6-2.2-1.8-2.8-2.8l.8-1.5-2-2z" fill="#fff"/></svg>
      0400 555 019
    </div>
  </article>
</section>

<!-- INSIDE -->
<section class="spread spread--inside">

  <article class="panel panel--profile">
    <svg class="deco" viewBox="0 0 247 540" preserveAspectRatio="none" aria-hidden="true">
      <path d="M0 0 L247 0 L247 40 Q120 60 0 95Z" fill="var(--sky)"/>
      <path d="M0 95 Q120 60 247 40 L247 52 Q120 72 0 105Z" fill="var(--blue)"/>
      <path d="M0 470 Q130 440 247 455 L247 540 L0 540Z" fill="var(--blue)"/>
      <path d="M0 492 Q130 465 247 478 L247 540 L0 540Z" fill="var(--navy)"/>
    </svg>
    <div class="layer" style="top:118px;padding:0 20px">
      <h2 class="name">Nina Ardell</h2>
      <p class="role">Exercise Physiologist</p>
      <p class="creds">B.AppSci – Human Mvmt<br>Grad Dip – ExRehab<br>Cert IV – Training &amp; Assessment</p>
      <p class="heal">Heal <b>through Movement</b></p>
      <p class="quote">Don't let the right exercise but the wrong technique hinder your recovery. Discover how important the correct exercise technique is to your success.</p>
    </div>
    <div class="photo photo--portrait" role="img" aria-label="Portrait photo of the physiologist">Portrait<br>Image Here</div>
  </article>

  <article class="panel panel--help">
    <svg class="deco" viewBox="0 0 247 540" preserveAspectRatio="none" aria-hidden="true">
      <rect width="247" height="540" fill="var(--pale)"/>
      <path d="M0 0 L247 0 L247 18 Q120 28 0 40Z" fill="var(--sky)"/>
      <path d="M0 40 Q120 28 247 18 L247 28 Q120 38 0 50Z" fill="var(--blue)"/>
    </svg>
    <div class="photo--runners" role="img" aria-label="Photo of a woman and a man running along a beach"></div>
    <div class="layer" style="top:64px;padding:0 18px">
      <p class="kicker">How can</p>
      <h2 class="headline" style="font-style:italic">I help you?</h2>
      <p class="body" style="font-size:8.5px;margin-top:10px">I have over 13 years of experience working as an Exercise Physiologist and have been working in the sport and fitness industry since 1996. I understand that everyone's health and exercise experience is unique and will tailor a program to suit you and your lifestyle.</p>
      <p class="body" style="font-size:8.5px;margin-top:6px">Managing your condition involves working with you to develop the best exercises and teaching you the correct technique essential to improve. Home and gym based programs can be provided.</p>
      <p class="body" style="font-size:8.5px;margin-top:6px">When appropriate I can also work with your current treating health practitioner to provide a holistic approach to your recovery.</p>
    </div>
  </article>

  <article class="panel panel--grey panel--conditions">
    <svg class="deco" viewBox="0 0 247 540" preserveAspectRatio="none" aria-hidden="true">
      <path d="M0 0 L247 0 L247 70 Q120 100 0 120Z" fill="var(--sky)"/>
      <path d="M0 120 Q120 100 247 70 L247 84 Q120 112 0 132Z" fill="var(--navy)"/>
      <circle cx="150" cy="240" r="95" fill="none" stroke="#d4dbe2" stroke-width="12"/>
      <path d="M0 470 Q130 440 247 430 L247 540 L0 540Z" fill="var(--sky)"/>
      <path d="M0 495 Q130 465 247 455 L247 540 L0 540Z" fill="var(--navy)"/>
    </svg>
    <div class="photo photo--legs" role="img" aria-label="Photo of legs running on grass"></div>
    <div class="layer" style="top:150px;padding:0 20px">
      <p style="font-size:11px">Common conditions that</p>
      <p style="font-size:11px;font-weight:700;color:var(--blue);font-style:italic">benefit from exercise therapy</p>
      <ul class="conditions">
        <li>Back pain</li>
        <li>Joint pain</li>
        <li>Pain relating to exercise</li>
        <li>Arthritis</li>
        <li>Anxiety relating to exercise</li>
        <li>Depression and Anxiety</li>
        <li>Chronic diseases such as diabetes, heart and lung disease</li>
        <li>Motor vehicle accidents</li>
      </ul>
      <p class="body" style="font-size:8px;margin-top:10px">Performing the right exercise the wrong way can do more harm than good. I can teach you what, how and when to perform your tailored exercise program to get the best results.</p>
    </div>
  </article>
</section>

</body>
</html>
```